Riverline Estate Holdings Co.

We need a logo and business card design for a Hong Kong based real estate company, KDT Land. We are want the brand to reflect the owners forward thinking, creative, and trend setting projects, while also reflecting a sense of security and strength. We invest in industrial properties which we convert to co-living or co-working spaces. KDT stands for Greater Bay Area which is the region around southern China including HK, Macau, and 9 other Chinese cities...made up of approx. 68 million people. There are massive infrastructure projects including the bridge to Macau and high-speed rail to SZ and the bridge connecting SZ and Zhongshan.

Target Market(s)

Chinese and western retail investors, as well as institutional investors

Industry/Entity Type

Real Estate Development

Contact Information for Business Card

Owen Tallis
CEO
owen@kdtland-hq.com
M + 852 9416 2057
F + 852 3582 0400
Suite 2207, The Meridale, 41 Larchmont Rd., Central, Hong Kong

Logo Text

kdt land (company name) lifestyle property development (underneath)

Colors

Designer to choose colors to be used in the design.

Requirements
Must have
• Details listed above. One side should include the logo and company name...kdt land in modern, hip styling with "lifestyle property development"
Nice to have
• Could be a Black card, with metallic purple "kdt" and white "land"...but open great design ideas
Should not have
• boring and traditional layout

```html
<!DOCTYPE html>
<html lang="en">
<head>
<meta charset="utf-8">
<title>KDT Land – Business Card</title>
<link rel="stylesheet" href="https://fonts.googleapis.com/css2?family=Open+Sans:wght@400;600&family=Roboto:wght@400&display=swap">
<style>
  :root {
    --backdrop: #2c3038;
    --card: #0b0b0c;
    --card-edge: #1a1a1c;
    --white: #ffffff;
    --purple: #8a5cc4;
    --muted: #bdbdc2;
    --rule: #5a5a5e;
  }
  * { margin: 0; padding: 0; box-sizing: border-box; }
  html, body { width: 1200px; height: 900px; overflow: hidden; }
  body {
    background: var(--backdrop);
    display: flex;
    flex-direction: column;
    align-items: center;
    justify-content: center;
    gap: 44px;
  }
  .card {
    width: 640px;
    height: 366px;
    background: var(--card);
    border: 1px solid var(--card-edge);
    position: relative;
    overflow: hidden;
  }
  .card-back .pattern-field {
    position: absolute;
    inset: 0;
    background: radial-gradient(ellipse at 40% 40%, #1c1c1f 0%, #0d0d0f 75%);
  }
  .brand-name {
    position: absolute;
    display: flex;
    align-items: center;
    gap: 16px;
    font-family: "Open Sans", sans-serif;
    font-weight: 600;
    color: var(--white);
    line-height: 1;
  }
  .brand-square {
    display: block;
    background: var(--purple);
  }
  .tagline {
    position: absolute;
    font-family: "Open Sans", sans-serif;
    font-weight: 400;
    color: var(--muted);
    text-transform: uppercase;
  }

  .card-back .brand-name { left: 70px; top: 140px; font-size: 72px; }
  .card-back .brand-square { width: 22px; height: 22px; }
  .card-back .tagline { left: 70px; bottom: 36px; font-size: 13px; letter-spacing: 3px; }

  .card-front .brand-name { left: 44px; top: 40px; font-size: 40px; gap: 12px; }
  .card-front .brand-square { width: 14px; height: 14px; }
  .card-front .tagline { right: 32px; bottom: 28px; font-size: 10px; letter-spacing: 2px; }

  .contact {
    position: absolute;
    left: 44px;
    top: 118px;
    width: 300px;
    text-align: center;
    font-family: "Roboto", sans-serif;
    color: var(--muted);
  }
  .contact-name {
    font-family: "Open Sans", sans-serif;
    font-weight: 600;
    font-size: 20px;
    color: var(--white);
    text-transform: uppercase;
    letter-spacing: 0.5px;
  }
  .contact-role {
    font-size: 17px;
    color: var(--purple);
    margin-top: 2px;
  }
  .contact-rule {
    width: 240px;
    height: 1px;
    background: var(--rule);
    margin: 8px auto;
  }
  .contact-line { font-size: 12.5px; line-height: 1.5; }
  .contact-dot {
    width: 5px; height: 5px; border-radius: 50%;
    background: var(--white);
    margin: 4px auto;
  }
</style>
</head>
<body>
  <section class="card card-back">
    <div class="pattern-field" role="img" aria-label="Faint repeated company name pattern across the card"></div>
    <p class="brand-name"><span class="brand-square"></span>KDT Land</p>
    <p class="tagline">Lifestyle Property Development</p>
  </section>

  <section class="card card-front">
    <p class="brand-name"><span class="brand-square"></span>KDT Land</p>
    <div class="contact">
      <p class="contact-name">Owen Tallis</p>
      <p class="contact-role">CEO</p>
      <div class="contact-rule"></div>
      <p class="contact-line">owen@kdtland-hq.com</p>
      <div class="contact-dot"></div>
      <p class="contact-line">M: + 852 9416 2057 | F: + 852 3582 0400</p>
      <div class="contact-dot"></div>
      <div class="contact-rule"></div>
      <p class="contact-line">Suite 2207, The Meridale, 41 Larchmont Rd.,<br>Central, Hong Kong</p>
    </div>
    <p class="tagline">Lifestyle Property Development</p>
  </section>
</body>
</html>
```